Business Card Design

We are a project managment company specializing in Interior fitout
PVH is for Commercial, Domestic, Industial - we provide managment to these industries and see the projects through design to contruction
Would like an area on the back of the card where peoplr can write notes
Thinking laser lines and architectural finishes
Colour theme at the moment is light grey and red although im open to any colour/design scheme

Industry/Entity Type

Business

Contact Information for Business Card

PVH Ventures
Brett Lamonte
Managing Director
0487215694
brett@pvhventures-example.com.au

```html
<!DOCTYPE html>
<html lang="en">
<head>
<meta charset="utf-8">
<title>Rallowby Ventures — Business Card</title>
<link rel="stylesheet" href="https://fonts.googleapis.com/css2?family=Bodoni+Moda:wght@600&family=Source+Sans+3:wght@400;500&display=swap">
<style>
  :root {
    --page-bg: #e9e9e9;
    --page-bg-edge: #cfcfcf;
    --card-blue: #2f48b0;
    --card-blue-light: #4a63c8;
    --card-blue-deep: #223a9c;
    --card-grey: #bdbdbd;
    --band-black: #0b0b0b;
    --name-blue: #2d46a8;
    --ink: #151515;
    --white: #ffffff;
  }
  html, body {
    margin: 0;
    width: 1200px;
    height: 1200px;
    overflow: hidden;
  }
  body {
    background: radial-gradient(circle at 50% 45%, #f7f7f7 0%, var(--page-bg) 45%, var(--page-bg-edge) 100%);
    position: relative;
  }
  .card {
    position: absolute;
    left: 100px;
    top: 322px;
    width: 1000px;
    height: 556px;
    box-shadow: 0 18px 40px rgba(0,0,0,0.18);
    overflow: hidden;
  }
  .card-shapes {
    position: absolute;
    inset: 0;
    width: 100%;
    height: 100%;
    display: block;
  }
  .company-name {
    position: absolute;
    left: 0;
    right: 0;
    top: 118px;
    margin: 0;
    text-align: center;
    padding-left: 60px;
    font-family: "Bodoni Moda", "Didot", serif;
    font-weight: 600;
    font-size: 56px;
    line-height: 1.2;
    color: var(--white);
    letter-spacing: 0.5px;
  }
  .person {
    position: absolute;
    left: 74px;
    top: 372px;
    text-align: right;
  }
  .person-name {
    margin: 0;
    font-family: "Source Sans 3", "Myriad Pro", sans-serif;
    font-weight: 400;
    font-size: 48px;
    line-height: 1;
    color: var(--name-blue);
  }
  .person-role {
    margin: 8px 0 0;
    font-family: "Source Sans 3", sans-serif;
    font-weight: 500;
    font-size: 25px;
    color: var(--ink);
    text-transform: uppercase;
  }
  .contacts {
    position: absolute;
    left: 540px;
    top: 404px;
    margin: 0;
    padding: 0;
    list-style: none;
    font-family: "Source Sans 3", sans-serif;
    font-size: 26px;
    color: var(--ink);
  }
  .contact-item {
    display: flex;
    align-items: center;
    gap: 14px;
    height: 46px;
    white-space: nowrap;
  }
  .contact-icon {
    width: 22px;
    height: 22px;
    flex: none;
  }
</style>
</head>
<body>
  <div class="card">
    <svg class="card-shapes" viewBox="0 0 1000 556" aria-hidden="true">
      <defs>
        <linearGradient id="blueGrad" x1="0" y1="0" x2="1" y2="1">
          <stop offset="0" stop-color="var(--card-blue-deep)"/>
          <stop offset="0.5" stop-color="var(--card-blue-light)"/>
          <stop offset="1" stop-color="var(--card-blue)"/>
        </linearGradient>
      </defs>
      <rect class="card-base" width="1000" height="556" fill="var(--card-grey)"/>
      <polygon class="accent-band" points="0,256 1000,256 1000,320 600,320 572,270 0,270" fill="var(--band-black)"/>
    </svg>
    <svg class="card-shapes" viewBox="0 0 1000 556" role="img" aria-label="Faint architectural floor plan drawing across the blue header">
      <rect class="header-panel" width="1000" height="258" fill="url(#blueGrad)"/>
    </svg>
    <h1 class="company-name">Rallowby Ventures</h1>
    <div class="person">
      <p class="person-name">Brett Lamonte</p>
      <p class="person-role">Managing Director</p>
    </div>
    <ul class="contacts">
      <li class="contact-item">
        <svg class="contact-icon" viewBox="0 0 24 24" aria-hidden="true"><path fill="var(--ink)" d="M6.6 10.8c1.4 2.8 3.8 5.1 6.6 6.6l2.2-2.2c.3-.3.7-.4 1-.2 1.1.4 2.3.6 3.6.6.6 0 1 .4 1 1V20c0 .6-.4 1-1 1C10.6 21 3 13.4 3 4c0-.6.4-1 1-1h3.5c.6 0 1 .4 1 1 0 1.2.2 2.4.6 3.6.1.3 0 .7-.2 1z"/></svg>
        <span class="contact-text">0491570156</span>
      </li>
      <li class="contact-item">
        <svg class="contact-icon" viewBox="0 0 24 24" aria-hidden="true"><rect x="2" y="5" width="20" height="14" fill="var(--ink)"/><path d="M3 6l9 7 9-7" fill="none" stroke="var(--card-grey)" stroke-width="1.8"/></svg>
        <span class="contact-text">brett@rallowby-example.com.au</span>
      </li>
    </ul>
  </div>
</body>
</html>
```